Other Setting Screens

Let's start with the new design of the rest of the pages of the app... All this pages are simple but let's keep the same type of design. You can find all this pages on the settings portion of the app. -My Posts-My Favorites-Premium Account-Edit Profile-Change Password-Leave Feedback

Colors
3176b5
0255a3
ffffff

```html
<!DOCTYPE html>
<html lang="en">
<head>
<meta charset="utf-8">
<title>Settings Screens</title>
<link href="https://fonts.googleapis.com/css2?family=Montserrat:wght@300;400;500;600;700&display=swap" rel="stylesheet">
<style>
:root{
  --blue:#3176b5;
  --navy:#0255a3;
  --white:#ffffff;
  --cyan:#22b4e6;
  --indigo:#2c3a8c;
  --bg:#e9ecef;
  --ink:#4a4f5a;
  --muted:#9aa0a8;
  --line:#e3e6ea;
  --field:#eef0fb;
  --star:#f7941d;
  --alert:#e0115f;
  --tile:#2a2d33;
}
*{box-sizing:border-box;margin:0;padding:0}
html,body{width:1200px;height:1109px;overflow:hidden}
body{background:var(--bg);font-family:"Montserrat",sans-serif;color:var(--ink);position:relative}
.phone{position:absolute;width:250px;height:510px;background:var(--white);border-radius:34px;box-shadow:0 18px 40px rgba(60,70,90,.14);overflow:hidden}
.screen{position:absolute;inset:0 0 62px 0;padding:26px 20px 0;overflow:hidden}
.title{font-size:13px;font-weight:500;text-align:center;color:var(--ink);letter-spacing:.3px}
.back{position:absolute;left:20px;top:24px;width:14px;height:14px}
.btn{display:block;margin:0 auto;width:160px;height:40px;border-radius:20px;border:0;background:linear-gradient(90deg,var(--cyan),var(--indigo));color:var(--white);font:500 12px "Montserrat",sans-serif;text-align:center;line-height:40px;box-shadow:0 8px 16px rgba(44,58,140,.25)}
.nav{position:absolute;left:0;right:0;bottom:0;height:62px;display:flex;justify-content:space-around;align-items:center;padding:0 10px;border-top:1px solid #f0f2f4;background:var(--white)}
.nav-item{display:flex;flex-direction:column;align-items:center;gap:3px;font-size:6px;letter-spacing:.3px;color:var(--ink);width:40px}
.nav-item.active{color:var(--cyan)}
.nav-item svg{width:16px;height:16px}
.nav-core{width:40px;height:40px;border-radius:50%;background:var(--white);box-shadow:0 4px 12px rgba(40,60,120,.2);display:flex;align-items:center;justify-content:center;margin-top:-22px}
.nav-core span{width:22px;height:22px;border-radius:50%;background:linear-gradient(135deg,var(--cyan),var(--indigo))}
.muted{color:var(--muted)}
/* favourites */
.brand-row{display:flex;justify-content:space-between;align-items:center;margin-bottom:14px}
.brand{font-size:20px;font-weight:600;color:var(--cyan);display:flex;align-items:center;gap:6px}
.brand i{width:12px;height:12px;border-radius:50%;background:var(--cyan);display:block}
.deal{background:var(--white);border-radius:14px;box-shadow:0 6px 16px rgba(60,70,90,.1);padding:10px 12px;margin-bottom:10px;position:relative}
.who{display:flex;gap:8px;align-items:center;font-size:9px;font-weight:600}
.who small{display:block;font-weight:400;font-size:7px;color:var(--muted)}
.avatar{width:22px;height:22px;border-radius:50%;background:linear-gradient(135deg,#8a8f98,#4d525a)}
.partner{margin-top:8px;font-size:14px;font-weight:500;color:#4b4ea8;display:flex;align-items:center;gap:5px}
.partner i{width:9px;height:9px;border-radius:50%;background:#4b4ea8;display:block}
.offer{margin-top:6px;font-size:9px;font-weight:600}
.stars{color:var(--star);font-size:10px;letter-spacing:1px}
.stars b{color:var(--ink);font-size:9px;margin-left:6px}
.deal .note{font-size:7px;color:var(--muted)}
.trash{position:absolute;right:12px;bottom:12px;width:10px;height:12px}
/* posts */
.posts-head{margin-bottom:4px}
.post{display:flex;gap:10px;margin-top:8px;border-radius:10px;box-shadow:0 6px 14px rgba(60,70,90,.1);overflow:hidden;height:62px;background:var(--white)}
.post-image{width:64px;flex:none;background:linear-gradient(135deg,#34373d,var(--tile))}
.post-body{padding:7px 8px 0 0;font-size:7px;color:var(--muted);line-height:1.35}
.post-body h4{font-size:8px;font-weight:600;color:var(--ink)}
.post-body h5{font-size:7px;font-weight:600;color:var(--ink);margin:2px 0}
/* verification */
.lead{font-size:11px;line-height:1.5;text-align:center;margin:26px 0 22px;color:var(--ink)}
.code{display:flex;justify-content:space-between;padding:0 6px}
.code span{width:36px;border-bottom:1px solid #555;text-align:center;font-size:22px;font-weight:300;color:var(--cyan);padding-bottom:8px}
.alert{color:var(--alert);font-size:8px;text-align:right;margin-top:8px}
.resend{font-size:9px;text-align:center;margin:30px 0 40px}
.resend a{color:var(--navy);font-weight:600}
/* change password */
.label{font-size:9px;color:var(--muted);margin:14px 0 6px}
.field{height:38px;border-radius:8px;background:var(--field)}
/* edit profile */
.cover{position:absolute;left:0;right:0;top:0;height:170px;background:linear-gradient(160deg,#6f6a6e 0%,#8d9680 55%,#c9cec6 100%)}
.cover-fade{position:absolute;left:0;right:0;top:120px;height:60px;background:linear-gradient(rgba(255,255,255,0),var(--white))}
.back.light{stroke:var(--white)}
.back.light path{stroke:var(--white)}
.profile-pic{position:absolute;left:50%;top:62px;transform:translateX(-50%);width:72px;height:72px;border-radius:50%;border:3px solid var(--white);background:linear-gradient(135deg,#b58a6a,#6d5440)}
.edit-title{position:absolute;top:24px;left:0;right:0;text-align:center;color:var(--white);font-size:12px;font-weight:500}
.premium-btn{position:absolute;top:152px;left:50%;transform:translateX(-50%);width:130px;height:30px;line-height:30px;font-size:9px;letter-spacing:.5px}
.info{position:absolute;top:206px;left:22px;right:22px}
.info dt{font-size:8px;font-weight:600;margin-top:8px}
.info dd{font-size:10px;padding:3px 0 6px;border-bottom:1px solid var(--line)}
.toggle-row{display:flex;justify-content:space-between;align-items:center;font-size:9px;font-weight:500;padding:8px 0;border-bottom:1px solid var(--line)}
.toggle{width:30px;height:16px;border-radius:8px;background:#e6e8ec;position:relative}
.toggle::after{content:"";position:absolute;right:2px;top:2px;width:12px;height:12px;border-radius:50%;background:var(--white);box-shadow:0 1px 3px rgba(0,0,0,.2)}
.toggle.on{background:linear-gradient(90deg,var(--cyan),var(--indigo))}
.toggle.on::after{right:auto;left:2px}
/* membership */
.plan{border-radius:18px;padding:16px 18px;margin-top:14px;position:relative;height:170px}
.plan h3{font-size:20px;font-weight:400}
.plan p{font-size:9px;font-weight:500}
.plan .price{font-size:32px;font-weight:300;margin-top:12px}
.plan .price small{font-size:10px;font-weight:500}
.plan.yearly{background:var(--cyan);color:var(--white)}
.plan.monthly{background:#eef4f9;color:var(--indigo)}
.plan .btn{position:absolute;left:50%;bottom:-14px;transform:translateX(-50%);width:130px;height:30px;line-height:30px;font-size:9px;letter-spacing:.5px}
/* feedback */
.rate{font-size:17px;font-weight:500;text-align:center;margin-top:30px}
.rate-sub{font-size:8px;text-align:center;color:var(--muted);margin-top:6px}
.big-stars{display:flex;justify-content:center;gap:8px;margin:30px 0}
.big-stars svg{width:26px;height:26px}
.comment{font-size:8px;color:var(--muted);border-bottom:1px solid #999;padding-bottom:70px;margin-bottom:40px}
</style>
</head>
<body>
<svg width="0" height="0" style="position:absolute">
  <defs>
    <symbol id="i-home" viewBox="0 0 16 16"><path d="M2 8 8 3l6 5v6H2z" fill="none" stroke="currentColor" stroke-width="1.3"/></symbol>
    <symbol id="i-msg" viewBox="0 0 16 16"><path d="M2 3h12v8H7l-3 3v-3H2z" fill="none" stroke="currentColor" stroke-width="1.3"/></symbol>
    <symbol id="i-bell" viewBox="0 0 16 16"><path d="M4 11V7a4 4 0 0 1 8 0v4l1 1H3z M7 13h2" fill="none" stroke="currentColor" stroke-width="1.3"/><circle cx="12.5" cy="4" r="2" fill="#e0115f"/></symbol>
    <symbol id="i-user" viewBox="0 0 16 16"><circle cx="8" cy="5.5" r="3" fill="none" stroke="currentColor" stroke-width="1.3"/><path d="M2.5 14a5.5 5.5 0 0 1 11 0" fill="none" stroke="currentColor" stroke-width="1.3"/></symbol>
    <symbol id="i-back" viewBox="0 0 14 14"><path d="M10 1 4 7l6 6" fill="none" stroke="currentColor" stroke-width="1.4"/></symbol>
    <symbol id="i-pin" viewBox="0 0 14 18"><circle cx="7" cy="6" r="4.5" fill="none" stroke="#3176b5" stroke-width="1.8"/><path d="M7 10.5V17" stroke="#3176b5" stroke-width="1.8"/></symbol>
    <symbol id="i-trash" viewBox="0 0 10 12"><rect x="1.5" y="3" width="7" height="8.5" rx="1" fill="none" stroke="#3176b5"/><path d="M0.5 2h9M4 0.8h2" stroke="#3176b5"/></symbol>
    <symbol id="i-star" viewBox="0 0 24 24"><path d="M12 1.5l3.2 6.9 7.3.8-5.4 5 1.5 7.3L12 17.8l-6.6 3.7 1.5-7.3-5.4-5 7.3-.8z"/></symbol>
  </defs>
</svg>

<!-- My Favorites -->
<section class="phone" style="left:40px;top:30px">
  <div class="screen">
    <div class="brand-row">
      <div class="brand"><i></i>Nuvo</div>
      <svg width="14" height="18"><use href="#i-pin"/></svg>
    </div>
    <article class="deal">
      <div class="who"><span class="avatar"></span><div>Dario Venn<small>2 hours ago</small></div></div>
      <div class="partner"><i></i>Skylark</div>
      <div class="offer">$50 Statement Credit</div>
      <div class="stars">★★★★★<b>4.5</b></div>
      <div class="note">$50 off on first order</div>
      <svg class="trash"><use href="#i-trash"/></svg>
    </article>
    <article class="deal">
      <div class="who"><span class="avatar"></span><div>Dario Venn<small>2 hours ago</small></div></div>
      <div class="partner"><i></i>Skylark</div>
      <div class="offer">$50 Statement Credit</div>
      <div class="stars">★★★★★<b>4.5</b></div>
      <div class="note">$50 off on first order</div>
      <svg class="trash"><use href="#i-trash"/></svg>
    </article>
    <article class="deal">
      <div class="offer">$50 Statement Credit</div>
      <div class="stars">★★★★★<b>4.5</b></div>
      <div class="note">$50 off on first order</div>
      <svg class="trash"><use href="#i-trash"/></svg>
    </article>
  </div>
  <nav class="nav">
    <div class="nav-item active"><svg><use href="#i-home"/></svg>HOME</div>
    <div class="nav-item"><svg><use href="#i-msg"/></svg>MESSAGES</div>
    <div class="nav-core"><span></span></div>
    <div class="nav-item"><svg><use href="#i-bell"/></svg>NOTIFICATION</div>
    <div class="nav-item"><svg><use href="#i-user"/></svg>PROFILE</div>
  </nav>
</section>

<!-- My Posts -->
<section class="phone" style="left:330px;top:30px">
  <div class="screen">
    <div class="brand-row posts-head">
      <svg width="16" height="16" viewBox="0 0 16 16"><path d="M1 1h5v5H1zM9 2h6M9 5h6M1 10h5v5H1zM9 11h6M9 14h6" fill="none" stroke="#3176b5" stroke-width="1.4"/></svg>
      <div class="title">Posts</div>
      <svg width="14" height="18"><use href="#i-pin"/></svg>
    </div>
    <article class="post"><div class="post-image" role="img" aria-label="Promotional image for the food delivery offer"></div><div class="post-body"><h4>Quick Bites | $20 OFF</h4><h5>DESCRIPTION</h5>Quick Bites is the easy way to get the food you love delivered.</div></article>
    <article class="post"><div class="post-image" role="img" aria-label="Promotional image for the food delivery offer"></div><div class="post-body"><h4>Quick Bites | $20 OFF</h4><h5>DESCRIPTION</h5>Quick Bites is the easy way to get the food you love delivered.</div></article>
    <article class="post"><div class="post-image" role="img" aria-label="Promotional image for the food delivery offer"></div><div class="post-body"><h4>Quick Bites | $20 OFF</h4><h5>DESCRIPTION</h5>Quick Bites is the easy way to get the food you love delivered.</div></article>
    <article class="post"><div class="post-image" role="img" aria-label="Promotional image for the food delivery offer"></div><div class="post-body"><h4>Quick Bites | $20 OFF</h4><h5>DESCRIPTION</h5>Quick Bites is the easy way to get the food you love delivered.</div></article>
    <article class="post"><div class="post-image" role="img" aria-label="Promotional image for the food delivery offer"></div><div class="post-body"><h4>Quick Bites | $20 OFF</h4><h5>DESCRIPTION</h5>Quick Bites is the easy way to get the food you love delivered.</div></article>
  </div>
  <nav class="nav">
    <div class="nav-item active"><svg><use href="#i-home"/></svg>HOME</div>
    <div class="nav-item"><svg><use href="#i-msg"/></svg>MESSAGES</div>
    <div class="nav-core"><span></span></div>
    <div class="nav-item"><svg><use href="#i-bell"/></svg>NOTIFICATION</div>
    <div class="nav-item"><svg><use href="#i-user"/></svg>PROFILE</div>
  </nav>
</section>

<!-- Change Password: verification -->
<section class="phone" style="left:620px;top:30px">
  <div class="screen">
    <div class="title">Change Password</div>
    <p class="lead">Enter your verification code we just send you to your mobile and email.</p>
    <div class="code"><span>4</span><span>0</span><span>3</span><span>2</span></div>
    <p class="alert">Password not match</p>
    <p class="resend muted">If you don't received ? <a>Resend</a></p>
    <div class="btn">Verify</div>
  </div>
  <nav class="nav">
    <div class="nav-item active"><svg><use href="#i-home"/></svg>HOME</div>
    <div class="nav-item"><svg><use href="#i-msg"/></svg>MESSAGES</div>
    <div class="nav-core"><span></span></div>
    <div class="nav-item"><svg><use href="#i-bell"/></svg>NOTIFICATION</div>
    <div class="nav-item"><svg><use href="#i-user"/></svg>PROFILE</div>
  </nav>
</section>

<!-- Edit Profile -->
<section class="phone" style="left:910px;top:30px">
  <div class="cover" role="img" aria-label="Blurred outdoor cover photo"></div>
  <div class="cover-fade"></div>
  <svg class="back" style="color:#ffffff"><use href="#i-back"/></svg>
  <div class="edit-title">Edit Profile</div>
  <div class="profile-pic" role="img" aria-label="Profile photo of the user"></div>
  <div class="btn premium-btn">GET PREMIUM</div>
  <dl class="info">
    <dt>Name</dt><dd>Lena Harlow</dd>
    <dt>City</dt><dd>Bristol, United Kingdom</dd>
    <dt>E-mail</dt><dd>lena.harlow@mailbox.com</dd>
    <div class="toggle-row">Show followers<span class="toggle"></span></div>
    <div class="toggle-row">Show photos<span class="toggle on"></span></div>
  </dl>
  <nav class="nav">
    <div class="nav-item active"><svg><use href="#i-home"/></svg>HOME</div>
    <div class="nav-item"><svg><use href="#i-msg"/></svg>MESSAGES</div>
    <div class="nav-core"><span></span></div>
    <div class="nav-item"><svg><use href="#i-bell"/></svg>NOTIFICATION</div>
    <div class="nav-item"><svg><use href="#i-user"/></svg>PROFILE</div>
  </nav>
</section>

<!-- Change Password: new password -->
<section class="phone" style="left:185px;top:570px">
  <div class="screen">
    <svg class="back" style="color:#3176b5"><use href="#i-back"/></svg>
    <div class="title">Change Password</div>
    <p class="lead" style="margin:22px 0 6px">Enter your new password below, we are just been extra security</p>
    <p class="label">Current Password</p><div class="field"></div>
    <p class="label">New Password</p><div class="field"></div>
    <p class="label">Confirm Password</p><div class="field"></div>
    <p class="alert">Password not match</p>
    <div class="btn" style="margin-top:16px">Change Password</div>
  </div>
  <nav class="nav">
    <div class="nav-item active"><svg><use href="#i-home"/></svg>HOME</div>
    <div class="nav-item"><svg><use href="#i-msg"/></svg>MESSAGES</div>
    <div class="nav-core"><span></span></div>
    <div class="nav-item"><svg><use href="#i-bell"/></svg>NOTIFICATION</div>
    <div class="nav-item"><svg><use href="#i-user"/></svg>PROFILE</div>
  </nav>
</section>

<!-- Upgrade Membership -->
<section class="phone" style="left:475px;top:570px">
  <div class="screen">
    <svg class="back" style="color:#3176b5"><use href="#i-back"/></svg>
    <div class="title">Upgrade Membership</div>
    <div class="plan yearly">
      <h3>Premium</h3><p>Annual Membership</p>
      <div class="price">$19.99<small>/Yearly</small></div>
      <div class="btn">UPGRADE NOW</div>
    </div>
    <div class="plan monthly" style="margin-top:26px">
      <h3>Premium</h3><p>Monthly Membership</p>
      <div class="price">$1.99<small>/Yearly</small></div>
      <div class="btn">UPGRADE NOW</div>
    </div>
  </div>
  <nav class="nav">
    <div class="nav-item active"><svg><use href="#i-home"/></svg>HOME</div>
    <div class="nav-item"><svg><use href="#i-msg"/></svg>MESSAGES</div>
    <div class="nav-core"><span></span></div>
    <div class="nav-item"><svg><use href="#i-bell"/></svg>NOTIFICATION</div>
    <div class="nav-item"><svg><use href="#i-user"/></svg>PROFILE</div>
  </nav>
</section>

<!-- Leave Feedback -->
<section class="phone" style="left:765px;top:570px">
  <div class="screen">
    <svg class="back" style="color:#3176b5"><use href="#i-back"/></svg>
    <div class="title">Leave Feedback</div>
    <h2 class="rate">Rate Your Experience</h2>
    <p class="rate-sub">Tell us about your experience with products</p>
    <div class="big-stars">
      <svg fill="#f7941d"><use href="#i-star"/></svg>
      <svg fill="#f7941d"><use href="#i-star"/></svg>
      <svg fill="#f7941d"><use href="#i-star"/></svg>
      <svg fill="#d3d6db"><use href="#i-star"/></svg>
      <svg fill="#d3d6db"><use href="#i-star"/></svg>
    </div>
    <p class="comment">Say something nice here</p>
    <div class="btn">Submit</div>
  </div>
  <nav class="nav">
    <div class="nav-item active"><svg><use href="#i-home"/></svg>HOME</div>
    <div class="nav-item"><svg><use href="#i-msg"/></svg>MESSAGES</div>
    <div class="nav-core"><span></span></div>
    <div class="nav-item"><svg><use href="#i-bell"/></svg>NOTIFICATION</div>
    <div class="nav-item"><svg><use href="#i-user"/></svg>PROFILE</div>
  </nav>
</section>
</body>
</html>
```